Quorvel Marketing & Design needs a Wordpress website

We need a wordpress design for a new marketing and design company in Australia called 'Quorvel Marketing & Design". The website needs to be responsive, modern, and attract new customers. It needs to be unique and different. We provide marketing and design solutions for small businesses from consulting, to flyer distribution to Facebook ads etc. We would like to see designs that use the Quorvel logo colours. The final design should communicate professionalism, creativity & growth. It needs to stand out from the crowd.

Target Market(s)

Small Business who need a marketing freelancer to help them grow

Industry/Entity Type

Marketing

Number of Pages Required

3 page

Requirements
Must have
• Home page, services page & contact page

```html
<!DOCTYPE html>
<html lang="en">
<head>
<meta charset="utf-8">
<title>Quorvel Marketing &amp; Design</title>
<link href="https://fonts.googleapis.com/css2?family=Raleway:wght@400;500;600;700&display=swap" rel="stylesheet">
<style>
:root{
  --magenta:#d6338f;
  --purple:#4a3a9c;
  --purple-dark:#2f2468;
  --navy:#2b2a5a;
  --text:#444;
  --muted:#777;
  --white:#fff;
}
*{box-sizing:border-box;margin:0;padding:0}
html,body{width:674px;height:1200px;overflow:hidden}
body{font-family:"Raleway",sans-serif;color:var(--text);background:var(--white);position:relative}
.header{position:absolute;top:0;left:0;width:674px;height:66px;background:var(--white)}
.brand{position:absolute;left:24px;top:21px;font-size:20px;font-weight:700;color:var(--purple-dark);line-height:24px;white-space:nowrap}
.contact-top{position:absolute;right:24px;top:20px;display:flex;gap:26px;font-size:12px;color:var(--muted);align-items:center}
.contact-top span{display:flex;align-items:center;gap:6px}
.nav{position:absolute;top:66px;left:0;width:674px;height:28px;background:var(--purple);display:flex;padding-left:60px}
.nav a{color:var(--white);text-decoration:none;font-size:11px;font-weight:600;padding:0 18px;line-height:28px;text-transform:uppercase}
.nav a.active{background:var(--magenta)}
.hero{position:absolute;top:94px;left:0;width:674px;height:278px;background:linear-gradient(180deg,#cfc6d8 0%,#b7a9c0 55%,#8f7d86 75%,#6e5d62 100%)}
.hero h1{position:absolute;left:24px;top:30px;font-size:40px;font-weight:400;color:var(--purple-dark);line-height:1.15}
.hero p{position:absolute;left:24px;top:132px;width:260px;font-size:11px;color:#3d3350;line-height:1.5}
.welcome{position:absolute;top:372px;left:0;width:674px;height:168px;text-align:center}
.welcome h2{margin-top:28px;font-size:28px;font-weight:500;color:#333}
.welcome h2 em{font-style:normal;color:var(--magenta)}
.rule{width:170px;height:2px;background:var(--magenta);margin:8px auto 12px}
.welcome p{width:340px;margin:0 auto;font-size:9px;line-height:1.5;color:var(--muted)}
.btn{display:inline-block;margin-top:14px;background:var(--magenta);color:var(--white);font-size:9px;font-weight:700;padding:6px 14px;text-transform:uppercase}
.services{position:absolute;top:540px;left:0;width:674px;height:371px;display:grid;grid-template-columns:1fr 1fr;grid-template-rows:1fr 1fr}
.service{position:relative;text-align:center;color:var(--white);padding-top:34px}
.s1{background:linear-gradient(135deg,#d94a9c,#b0307d)}
.s2{background:linear-gradient(135deg,#2e2c63,#3f3a82)}
.s3{background:linear-gradient(135deg,#5a4aa8,#3d2f86)}
.s4{background:linear-gradient(135deg,#c83596,#9c2a85)}
.icon{width:56px;height:56px;border-radius:50%;background:var(--white);margin:0 auto 8px;display:flex;align-items:center;justify-content:center}
.icon i{width:30px;height:30px;border-radius:50%;display:block}
.service h3{font-size:15px;font-weight:500;margin-bottom:6px}
.service p{width:160px;margin:0 auto;font-size:9px;line-height:1.45}
.contact{position:absolute;top:911px;left:0;width:674px;height:214px}
.form-area{position:absolute;left:0;top:0;width:337px;height:214px;background:linear-gradient(135deg,#6f7a5e,#4d5a44)}
.field{position:absolute;left:86px;width:204px;height:22px;border:1px solid rgba(255,255,255,.8);background:rgba(255,255,255,.12);color:var(--white);font-size:9px;padding:5px 6px}
.send{position:absolute;left:86px;top:172px;width:204px;height:24px;background:var(--magenta);color:var(--white);font-size:14px;text-align:center;line-height:24px}
.map{position:absolute;left:337px;top:0;width:337px;height:214px;background:linear-gradient(135deg,#d9d6dc,#bdb8c4)}
.info{position:absolute;left:446px;top:78px;width:200px;height:80px;background:rgba(74,58,156,.85);color:var(--white);font-size:9px;padding:8px 10px;line-height:2.1;white-space:nowrap}
.info div{display:flex;align-items:center;gap:6px}
.pin{position:absolute;left:402px;top:80px}
.footer{position:absolute;top:1125px;left:0;width:674px;height:75px;text-align:center;font-size:9px;color:#555}
.footer nav{margin-top:22px}
.footer nav span{padding:0 12px;border-right:1px solid #bbb}
.footer nav span:last-child{border:0}
.footer p{margin-top:12px;color:var(--muted)}
.footer p b{color:var(--magenta);font-weight:500}
</style>
</head>
<body>
<header class="header">
  <div class="brand">Quorvel Marketing &amp; Design</div>
  <div class="contact-top">
    <span><svg width="12" height="9" viewBox="0 0 12 9"><rect width="12" height="9" fill="#555"/><path d="M0 0 6 5 12 0" stroke="#fff" fill="none"/></svg>info@quorvel.com</span>
    <span><svg width="10" height="12" viewBox="0 0 10 12"><rect x="1" y="0" width="8" height="12" rx="1.5" fill="#555"/></svg>02 9876 5432</span>
  </div>
</header>
<nav class="nav">
  <a class="active" href="#">Home</a><a href="#">Our Services</a><a href="#">Clients</a><a href="#">About Us</a><a href="#">Contact Us</a>
</nav>
<section class="hero" role="img" aria-label="Businessman seated on a wooden deck working on a laptop, with floating icons above a bright sky">
  <h1>We Make You Look<br>Good.</h1>
  <p>Lorem Ipsum is simply dummy text of the printing and typesetting industry.</p>
</section>
<section class="welcome">
  <h2>Welcome to Quorvel <em>Marketing &amp; Design</em></h2>
  <div class="rule"></div>
  <p>Looking for some marketing expertise or have you started your own business and ready to take the plunge in getting your name out there. You've come to the right place!</p>
  <span class="btn">Know More</span>
</section>
<section class="services">
  <div class="service s1"><div class="icon" role="img" aria-label="Colour wheel icon"><i style="background:conic-gradient(#e63c3c,#f2c12e,#3cb44b,#2e7bd6,#b43cb4,#e63c3c)"></i></div><h3>Logo Design</h3><p>Lorem Ipsum is simply dummy text of the printing and typesetting industry.</p></div>
  <div class="service s2"><div class="icon" role="img" aria-label="Business card icon"><i style="background:#d6338f;border-radius:4px"></i></div><h3>Corporate Identity</h3><p>Lorem Ipsum is simply dummy text of the printing and typesetting industry.</p></div>
  <div class="service s3"><div class="icon" role="img" aria-label="Folded flyer icon"><i style="background:#4a6cc4;border-radius:3px"></i></div><h3>Flyers</h3><p>Lorem Ipsum is simply dummy text of the printing and typesetting industry.</p></div>
  <div class="service s4"><div class="icon" role="img" aria-label="Group of consultants icon"><i style="background:#f08a2c"></i></div><h3>Consulting</h3><p>Lorem Ipsum is simply dummy text of the printing and typesetting industry.</p></div>
</section>
<section class="contact">
  <div class="form-area" role="img" aria-label="Softly blurred office background behind the contact form"></div>
  <div class="field" style="top:18px">Name</div>
  <div class="field" style="top:48px">E Mail</div>
  <div class="field" style="top:78px;height:80px">Message</div>
  <div class="send">Send</div>
  <div class="map" role="img" aria-label="Street map showing the office location"></div>
  <svg class="pin" width="22" height="30" viewBox="0 0 22 30"><path d="M11 0a11 11 0 0 1 11 11c0 8-11 19-11 19S0 19 0 11A11 11 0 0 1 11 0z" fill="#4a3a9c"/><circle cx="11" cy="11" r="4" fill="#fff"/></svg>
  <div class="info">
    <div>● 204, Office plaza name City Country</div>
    <div>● 02 9876 5432</div>
    <div>● info@quorvel.com</div>
  </div>
</section>
<footer class="footer">
  <nav><span>Privacy</span><span>Terms &amp; Conditions</span><span>FAQs</span></nav>
  <p><b>© Quorvel</b> 2015. All Rights Reserved</p>
</footer>
</body>
</html>
```